Every Muse Stage Academy Leaflet - Kids classes

I would like a leaflet designed for my classes, with a clear and informative time table on the back:

I have attached a couple of adverts that we have used in the local News Paper and on Chatterbook, and so the front side of the leaflet should be something similar using the plain Y spark photo:

Wording on the front with the photo should be

'Every Muse Stage Academy Ltd! As featured on The Bright Spark Grand Showdown'

Wording 'We offer AFFORDABLE, professional, accredited training in Drama, Singing and Dance for ages 3- 18 years. FREE casting Agency, Optional RQPV & HWSO exams and Unparalleled performance opportunities.

WWW. EVERYMUSESTAGE.EXAMPLE / 020 7946 0173

Chatterbook : www.chatterbook.example/everymusestage

BOOK your Trial Today!

BACK SIDE

I would like a clear timetable designed with the following info

Classes

Tiny Sparks - Ages 3-5 years - Drama, Singing & Dance
from Quellory to Pop in one fast paced fun & imaginative session with regular confidence building shows £4

Drama, Song & Dance Ages 6-10 years - 90 minutes of complete theatrical training taught by qualified industry experts with the opportunity to take RQPV & HWSO Dance exams, regular shows and local events £8.50

Drama, Song & Dance Ages 11- 18years - 90 minutes of advanced level Drama, Singing and Dance. RQPV & HWSO dance exams , shows, competitions and audition preparation for colleges and castings. This session is a one stop shop for professional theatrical training.

EMS MT ( Musical Theatre) - Ages 6-10years - 90 minutes of Musical Theatre training covering classic musicals including hits such as Tilda, Ferro & Bandroom Rebels. Musical Theatre Singing exams and RQPV drama are included in this popular fast paced session.

EMS MT ( Musical Theatre) - Ages 11- 18years - 90 minutes of professional Musical Theatre training with an emphasis on singing. These Chime- Style sessions are ideal for those who love musicals such as Verdant, Quiffs & Grand Ringmaster. Our advanced MT sessions produce high quality songs & medleys for shows and competitions as well as Musical Theatre/ Singing exams and Solo RQPV training.

Weekend Footlights Company - Ages 4-18years - 4 hours of professional training, working towards a production. This unique group gives young performers the opportunity to perform in a full scale production EVERY term. Past shows include 'Twin Crossings', 'Kelpa', 'Tiny Store of Frights', 'Fennick & Marisol' and 'Quellory Heirlings' At EMS we believe that pupils learn through actual performing experience, there is a role for everyone, full costume and the chance to shine on stage!

Day : Tuesdays
Venue: Holm Oak Hall - Marrowdale
Sessions:
4:45-5:15pm - Tiny Sparks
5:15-6:45pm - Drama, Song & Dance ages 6-10 years
6:45- 8:15pm - Drama, Song & Dance ages 11- 18years

Day : Wednesdays
Venue : Ashgrove Hall - Brackley Green Village
3:45-4:15pm - Tiny Sparks
4:30-6:00pm - EMS MT ages 6-10 years
6:00-7:30pm - EMS MT ages 11-18 years

Day: Fridays
Venue : The Hub, 217 Pellingham Lane New Elmsworth
4:15-4:45 - Tiny Sparks
4:45-6:15pm - Drama, Song & Dance ages 6-10 years
6:15- 7:45pm - Drama, Song & Dance ages 11- 18years

Day: Saturdays
10am-2pm - Weekend Footlights Company ages 4-18 years
Junior & Senior groups

Target Market(s)

Parents and children ages 10- 18years

Industry/Entity Type

Performing Art

Colors
e34297
f04a50
f68e4e
faa54b

Requirements
Must have
• A full time table & class descriptions on the back
• Be bright and eye catching
• Bold wording
• Company logos as well as RQPV logo & HWSO logo & PLOV logo
Nice to have
• Large pot ( the Y spark one)
Should not have
• Look too cluttered

```html
<!DOCTYPE html>
<html lang="en">
<head>
<meta charset="utf-8">
<title>Every Muse Stage Academy – Timetable</title>
<link href="https://fonts.googleapis.com/css2?family=Montserrat:wght@400;500;600;700&display=swap" rel="stylesheet">
<style>
  :root{
    --pink:#e34297;
    --red:#f04a50;
    --orange:#f68e4e;
    --amber:#faa54b;
    --ink:#2f2f2f;
    --soft-ink:#444;
    --card:#f1eee8;
    --pill:#ecebe7;
    --page:#e6e1d9;
  }
  *{box-sizing:border-box;margin:0;padding:0}
  html,body{width:1200px;height:1200px;overflow:hidden}
  body{background:var(--page);font-family:"Montserrat",sans-serif;color:var(--ink);position:relative}
  .leaflet{position:absolute;left:30px;top:160px;width:1328px;height:1026px;background:var(--card);
    transform:scale(0.8584);transform-origin:0 0;box-shadow:0 6px 18px rgba(0,0,0,.18);overflow:hidden}
  .stage-backdrop{position:absolute;left:0;top:0;width:1328px;height:640px;
    background:radial-gradient(ellipse at 60% 55%,rgba(170,165,158,.22),rgba(241,238,232,0) 70%),
               linear-gradient(180deg,rgba(241,238,232,0),rgba(190,184,176,.18) 80%,rgba(241,238,232,0));}
  .brand{position:absolute;left:42px;top:40px;display:flex;align-items:center;gap:10px;width:260px}
  .brand-dot{width:26px;height:26px;border-radius:50%;background:var(--amber);flex:none}
  .brand-name{color:var(--red);font-weight:700;font-size:21px;line-height:1.15}
  .pin{position:absolute;left:310px;top:28px}
  .arrow{position:absolute;top:58px}
  .day{position:absolute;top:38px;width:220px;text-align:center;font-size:16.5px;line-height:20px;color:var(--soft-ink)}
  .day h3{color:var(--red);font-weight:600;font-size:20px;line-height:24px}
  .row-label{position:absolute;left:50px;font-size:19.5px;line-height:24px;color:var(--soft-ink)}
  .row-label b{display:block;color:var(--pink);font-weight:500}
  .row-line{position:absolute;left:381px;width:897px;height:1.6px;background:#222}
  .pill{position:absolute;width:190px;height:38px;margin-top:-19px;border:1.6px solid #333;border-radius:19px;
    background:var(--pill);font-size:20.5px;line-height:35px;text-align:center;color:var(--ink)}
  .pill.wide{width:208px}
  .info{position:absolute;width:383px;font-size:14.6px;line-height:18.1px;text-align:justify;color:var(--ink)}
  .info h4{font-size:16px;font-weight:600;line-height:20px;text-align:left;margin-bottom:0}
  .info p+h4{margin-top:17px}
  .tag{position:absolute;height:29px;border-radius:15px;background:var(--amber);color:#222;
    font-weight:600;font-size:19px;line-height:29px;padding-left:18px}
  .accreditations{position:absolute;left:468px;top:926px;display:flex;gap:22px;align-items:center}
  .accred{display:flex;align-items:center;gap:7px;font-weight:700;font-size:30px;color:var(--pink)}
  .accred i{display:block;width:16px;height:16px;background:var(--pink)}
</style>
</head>
<body>
<main class="leaflet">
  <div class="stage-backdrop" role="img" aria-label="Faint photo of performers on a large stage set"></div>

  <div class="brand"><span class="brand-dot"></span><span class="brand-name">Every Muse Stage Academy</span></div>

  <svg class="pin" width="58" height="86" viewBox="0 0 58 86" aria-hidden="true">
    <path d="M29 2C14 2 2 14 2 29c0 20 27 55 27 55s27-35 27-55C56 14 44 2 29 2z" fill="#e8493f"/>
    <circle cx="29" cy="27" r="11" fill="#f1eee8"/>
  </svg>

  <svg class="arrow" style="left:389px" width="38" height="28" viewBox="0 0 38 28" aria-hidden="true"><path d="M2 9h20V2l14 12-14 12v-7H2z" fill="none" stroke="#333" stroke-width="1.6"/></svg>
  <svg class="arrow" style="left:596px" width="38" height="28" viewBox="0 0 38 28" aria-hidden="true"><path d="M2 9h20V2l14 12-14 12v-7H2z" fill="none" stroke="#333" stroke-width="1.6"/></svg>
  <svg class="arrow" style="left:809px" width="38" height="28" viewBox="0 0 38 28" aria-hidden="true"><path d="M2 9h20V2l14 12-14 12v-7H2z" fill="none" stroke="#333" stroke-width="1.6"/></svg>
  <svg class="arrow" style="left:1023px" width="38" height="28" viewBox="0 0 38 28" aria-hidden="true"><path d="M2 9h20V2l14 12-14 12v-7H2z" fill="none" stroke="#333" stroke-width="1.6"/></svg>

  <div class="day" style="left:397px"><h3>Tuesdays</h3>Holm Oak Hall<br>Marrowdale</div>
  <div class="day" style="left:611px"><h3>Wednesdays</h3>Ashgrove Hall<br>Brackley Green Village</div>
  <div class="day" style="left:824px"><h3>Fridays</h3>The Hub,<br>217 Pellingham Lane<br>New Elmsworth</div>
  <div class="day" style="left:1039px"><h3>Saturdays</h3>The Hub,<br>217 Pellingham Lane<br>New Elmsworth</div>

  <div class="row-label" style="top:138px"><b>Tiny Sparks</b>(Ages 3-5 years)</div>
  <div class="row-label" style="top:210px"><b>Drama, Song &amp; Dance</b>(Ages 6-10 years)</div>
  <div class="row-label" style="top:283px"><b>Drama, Song &amp; Dance</b>(Ages 11- 18years)</div>
  <div class="row-label" style="top:355px"><b>EMS MT</b>(Ages 6-10 years)</div>
  <div class="row-label" style="top:428px"><b>EMS MT</b>(Ages 11-18 years)</div>
  <div class="row-label" style="top:500px"><b>Weekend Footlights Company</b>(Ages 4-18 years)</div>

  <div class="row-line" style="top:150px"></div>
  <div class="row-line" style="top:222px"></div>
  <div class="row-line" style="top:295px"></div>
  <div class="row-line" style="top:367px"></div>
  <div class="row-line" style="top:440px"></div>
  <div class="row-line" style="top:512px"></div>

  <div class="pill" style="left:412px;top:150px">4:45pm - 5:15pm</div>
  <div class="pill" style="left:626px;top:150px">3:45pm - 4:15pm</div>
  <div class="pill" style="left:839px;top:150px">4:15pm - 4:45pm</div>
  <div class="pill" style="left:412px;top:222px">5:15pm - 6:45pm</div>
  <div class="pill" style="left:839px;top:222px">4:45pm - 6:15pm</div>
  <div class="pill" style="left:412px;top:295px">6:45pm - 8:15pm</div>
  <div class="pill" style="left:839px;top:295px">6:15pm - 7:45pm</div>
  <div class="pill" style="left:626px;top:367px">4:30pm - 6:00pm</div>
  <div class="pill" style="left:626px;top:440px">6:00pm - 7:30pm</div>
  <div class="pill wide" style="left:1044px;top:511px">10:00am - 2:00pm</div>

  <div class="tag" style="left:33px;top:613px;width:155px">Tiny Sparks</div>
  <div class="tag" style="left:452px;top:613px;width:266px">Drama, Song &amp; Dance</div>
  <div class="tag" style="left:882px;top:613px;width:328px">EMS MT (Musical Theatre)</div>
  <div class="tag" style="left:33px;top:759px;width:353px">Weekend Footlights Company</div>

  <div class="info" style="left:52px;top:660px">
    <h4>Ages 3-5 years</h4>
    <p>Drama, Singing &amp; Dance from Quellory to Pop in one fast paced fun &amp; imaginative session with regular confidence building shows £4</p>
  </div>
  <div class="info" style="left:52px;top:805px">
    <h4>Ages 4-18years</h4>
    <p>4 hours of professional training, working towards a production. This unique group gives young performers the opportunity to perform in a full scale production EVERY term. Past shows include 'Twin Crossings', 'Kelpa', 'Tiny Store of Frights', 'Fennick &amp; Marisol' and 'Quellory Heirlings' At EMS we believe that pupils learn through actual performing experience, there is a role for everyone, full costume and the chance to shine on stage!</p>
  </div>
  <div class="info" style="left:471px;top:660px">
    <h4>Ages 6-10 years</h4>
    <p>90 minutes of complete theatrical training taught by qualified industry experts with the opportunity to take RQPV &amp; HWSO Dance exams, regular shows and local events £8.50</p>
    <h4>Ages 11- 18years</h4>
    <p>90 minutes of advanced level Drama, Singing and Dance. RQPV &amp; HWSO dance exams , shows, competitions and audition preparation for colleges and castings. This session is a one stop shop for professional theatrical training.</p>
  </div>
  <div class="info" style="left:901px;top:660px">
    <h4>Ages 6-10 years</h4>
    <p>90 minutes of Musical Theatre training covering classic musicals including hits such as Tilda, Ferro &amp; Bandroom Rebels. Musical Theatre Singing exams and RQPV drama are included in this popular fast paced session.</p>
    <h4>Ages 11- 18years</h4>
    <p>90 minutes of professional Musical Theatre training with an emphasis on singing. These Chime- Style sessions are ideal for those who love musicals such as Verdant, Quiffs &amp; Grand Ringmaster. Our advanced MT sessions produce high quality songs &amp; medleys for shows and competitions as well as Musical Theatre/ Singing exams and Solo RQPV training.</p>
  </div>

  <div class="accreditations">
    <span class="accred">RQPV</span>
    <span class="accred"><i></i>HWSO</span>
    <span class="accred"><i></i>PLOV</span>
  </div>
</main>
</body>
</html>
```